Premium modern eliquids labels 84.5 x 80 mm

I am looking for modern graphics for the labels of a new eliquid line that will have 4 different types of eliquids. It will have a tobacco one (brown colours maybe), a fruity one (bright colours maybe), a minty one (green colours maybe) and a creamy one (beige colours maybe).
I will need one of them to see how the design is, that design will have to be adapted to the other 3 colours of the label.
The brand logo is attached. I also attached a sample of what is mandatory to write on the label, you can change size, place and font of what is written, the only thing that cannot be reduced is the yellow parts. I attach the bottle that we will use.The size of the label is 84.5 x 80 mm (base x height).

Target Market(s)

vapers

Requirements
Must have
• My project must have one of the labels.

```html
<!DOCTYPE html>
<html lang="it">
<head>
<meta charset="utf-8">
<title>Lumen Drops – Fruit Flavored label</title>
<link href="https://fonts.googleapis.com/css2?family=Open+Sans:wght@400;600;700;800&display=swap" rel="stylesheet">
<style>
  :root{
    --page:#ffffff;
    --ink:#2b2b2b;
    --strip:#262626;
    --lime-light:#eef8d2;
    --lime:#b7e25a;
    --lime-deep:#6cc11a;
    --brand:#6eb4e6;
    --badge:#f9c23c;
  }
  *{box-sizing:border-box;margin:0;padding:0}
  html,body{width:1200px;height:2367px;overflow:hidden;background:var(--page)}
  body{font-family:'Open Sans',sans-serif;color:var(--ink);position:relative}

  .label{
    position:absolute;left:162px;top:774px;width:865px;height:818px;
    background:linear-gradient(180deg,#ffffff 0%,#ffffff 8%,var(--lime-light) 38%,var(--lime) 72%,var(--lime-deep) 100%);
    overflow:hidden;
  }
  .lot-strip{
    position:absolute;left:0;top:0;width:47px;height:100%;background:var(--strip);
    display:flex;align-items:center;justify-content:center;
  }
  .lot-strip span{
    transform:rotate(-90deg);white-space:nowrap;color:#fff;font-weight:700;font-size:21px;letter-spacing:.2px;
  }
  .block-title{font-weight:700;font-size:20px;line-height:30px}
  .body-text{font-size:20px;line-height:29px}

  .ingredients{position:absolute;left:67px;top:94px;width:200px}
  .producer{position:absolute;left:67px;top:506px;width:240px}
  .producer .block-title{line-height:29px}
  .instructions{position:absolute;left:619px;top:112px;width:230px}

  .brand-name{
    position:absolute;left:280px;top:122px;width:300px;text-align:center;
    font-weight:800;font-size:34px;letter-spacing:1px;color:var(--brand);
  }
  .fruit-art{
    position:absolute;left:295px;top:248px;width:275px;height:263px;border-radius:48%;
    background:radial-gradient(circle at 50% 55%,#f2a33a 0%,#e86a3a 30%,#9bc540 55%,rgba(183,226,90,0) 72%);
  }
  .script-word{
    position:absolute;left:324px;top:529px;width:228px;height:118px;border-radius:10px;
    background:linear-gradient(90deg,rgba(30,40,20,.55),rgba(30,40,20,.35));
  }
  .flavored{
    position:absolute;left:352px;top:638px;font-size:16px;letter-spacing:11px;color:var(--ink);
  }
  .net{position:absolute;left:280px;top:722px;width:300px;text-align:center;font-weight:700;font-size:22px}

  .badge{position:absolute;left:619px;background:var(--badge);font-weight:700;color:var(--ink)}
  .badge.small{width:120px;height:37px;font-size:13px;line-height:14px;padding:5px 0 0 12px}
  .badge.code{width:85px;height:36px;font-size:20px;line-height:36px;padding-left:10px}
  .badge-caption{position:absolute;left:619px;font-size:16px}
  .badge-caption.bold{font-weight:700}

  .disposal-icons{position:absolute;left:617px;top:684px}
</style>
</head>
<body>
  <section class="label">
    <div class="lot-strip"><span>L.SH20 - 001-PES-D.PROD.22-04-2022 D.SC.21-04-2024</span></div>

    <div class="ingredients">
      <p class="block-title">INGREDIENTI:</p>
      <p class="body-text">Glicolepropilenico sostanzearomatiz zanti</p>
    </div>

    <div class="brand-name">LUMEN DROPS</div>
    <div class="fruit-art" role="img" aria-label="Illustration of mixed fruit: pineapple, orange, kiwi, plum, mango, pear, strawberry and banana"></div>
    <div class="script-word" role="img" aria-label="Hand-lettered script word 'fruit'"></div>
    <div class="flavored">FLAVORED</div>
    <div class="net">20 ML NET</div>

    <div class="producer">
      <p class="block-title">PRODOTTO<br>E CONFEZIONATO</p>
      <p class="body-text"><strong>DA</strong> Veltra srl<br>Via Garibaldi 57<br>10122 Torino<br>P.i.01234567890<br>Tel. +39 011 5550142<br>info@veltra.it</p>
    </div>

    <div class="instructions">
      <p class="block-title">ISTRUZIONI D’USO:</p>
      <p class="body-text">Agitare bene prima dell’utilizzo. Diluire nelle percentuali consigliate sul nostro sito. Conservare in luogo fresco e asciutto</p>
    </div>

    <div class="badge small" style="top:400px">RACCOLTA<br>PLASTICA</div>
    <div class="badge-caption bold" style="top:438px">ETICHETTA</div>
    <div class="badge code" style="top:461px">PAP 5</div>

    <div class="badge small" style="top:524px">RACCOLTA<br>PLASTICA</div>
    <div class="badge-caption" style="top:561px">FLACONE</div>
    <div class="badge code" style="top:587px">PET 1</div>

    <svg class="disposal-icons" width="140" height="64" viewBox="0 0 140 64" aria-label="Recycle and dispose in bin icons">
      <g fill="none" stroke="#2b2b2b" stroke-width="3" stroke-linejoin="round" stroke-linecap="round">
        <path d="M24 10 L34 10 L42 24"/><path d="M38 22 L42 24 L44 19"/>
        <path d="M48 34 L54 46 L44 54"/><path d="M48 52 L44 54 L46 58"/>
        <path d="M30 56 L12 56 L8 44"/><path d="M10 48 L8 44 L4 46"/>
        <path d="M20 12 L10 30"/><path d="M50 40 L40 40"/>
      </g>
      <g fill="#2b2b2b">
        <path d="M76 28 h30 l-4 34 h-22 z"/>
        <rect x="73" y="23" width="36" height="4"/>
        <rect x="118" y="6" width="8" height="56" rx="3"/>
        <circle cx="122" cy="6" r="5"/>
        <rect x="86" y="12" width="8" height="8"/>
      </g>
    </svg>
  </section>
</body>
</html>
```